We have a cheerleading competition on Sunday the 30 and I want to encourage parent assistance, support and participation!
Updates

1. Please add:
    Cheer Championship (instead of Cheerleading Competition)

2. Banner: Let's support our Cheerleaders!

Under Banner have the Date in big

Before the Location add:  Joins us at:

Thank you all for your designs and taking the time to submit them. I greatly appreciate them and they were all lovely. I could only pick one though! Hope to have you again on my next project.

Regards, Marisa

Industry/Entity Type

It Support

Requirements
Must have
• Flyer should be 1/2 of an A4 page. kid friendly. The cheerleaders are 6-13 yrs old.
The colors Burgundy, Gold (yellow) and White - It should have the team Eagle design on it. Tarpon Ridge Falcons

Simple design. It will contain an address, times and dates.

should have all of the following information:

Date: Sunday - October 30th 2011
Location: Harbor Crest Arena at the Pellham Coast College
3870 Kestrel Lane
Coral gables, FL 33146
Time: Tickets on sale 8:30AM - Doors Open 9:00AM Starts: 10:00AM
Prices: Adults $10.00 Children $5.00 - Cash Only

```html
<!DOCTYPE html>
<html lang="en">
<head>
<meta charset="utf-8">
<title>Cheer Championship Flyer</title>
<link rel="stylesheet" href="https://fonts.googleapis.com/css2?family=Graduate&family=Oswald:wght@600&display=swap">
<style>
  :root {
    --burgundy: #c8161d;
    --burgundy-deep: #9d0f15;
    --gold: #ffe500;
    --gold-deep: #ffd200;
    --white: #ffffff;
    --ink: #1a1a1a;
    --shadow-grey: #b9b9b9;
    --frame: #8a8a8a;
  }
  * { margin: 0; padding: 0; box-sizing: border-box; }
  html, body {
    width: 1200px; height: 846px; overflow: hidden;
    background: var(--white);
  }
  .sheet { position: relative; width: 1200px; height: 846px; }
  .flyer {
    position: absolute; top: 29px;
    width: 571px; height: 787px;
    background: var(--white);
    border: 1px solid var(--frame);
    overflow: hidden;
    font-family: "Graduate", serif;
    color: var(--burgundy);
  }
  .flyer--left { left: 29px; }
  .flyer--right { left: 600px; border-left: none; }
  .flyer__backdrop { position: absolute; inset: 0; width: 100%; height: 100%; }

  .cheer-squad {
    position: absolute; left: 106px; top: 33px; width: 360px; height: 157px;
    background: radial-gradient(ellipse at 50% 45%, #d8262b 0%, #c8161d 45%, rgba(200,22,29,0.15) 75%, rgba(200,22,29,0) 100%);
    border-radius: 40% 40% 30% 30%;
  }

  .headline {
    position: absolute; left: 0; width: 100%; text-align: center;
    color: var(--burgundy);
    text-shadow:
      2px 0 0 var(--white), -2px 0 0 var(--white), 0 2px 0 var(--white), 0 -2px 0 var(--white),
      3px 5px 0 var(--shadow-grey);
    letter-spacing: 1px;
  }
  .headline--cheer { top: 200px; font-size: 52px; }
  .headline--championship { top: 268px; font-size: 50px; letter-spacing: 0; }

  .banner { position: absolute; left: 58px; top: 330px; width: 456px; height: 100px; }

  .event-date { position: absolute; left: 0; width: 100%; text-align: center; color: var(--burgundy); line-height: 1; }
  .event-date__day { top: 441px; font-size: 28px; }
  .event-date__month { top: 470px; font-size: 42px; }
  .event-date__year { top: 515px; font-size: 36px; }

  .mascot {
    position: absolute; left: 229px; top: 546px; width: 112px; height: 74px;
    background: linear-gradient(135deg, #a0141a 0%, #c8161d 55%, #f2b400 100%);
    border-radius: 50% 45% 40% 55%;
  }

  .venue { position: absolute; left: 0; top: 632px; width: 100%; text-align: center; }
  .venue__lead { font-size: 12.5px; color: var(--burgundy); }
  .venue__line { font-size: 12.5px; color: var(--ink); line-height: 15px; }

  .details { position: absolute; top: 697px; font-size: 12.5px; line-height: 15.5px; color: var(--ink); }
  .details--time { left: 40px; }
  .details--prices { left: 272px; }
  .details__label { color: var(--burgundy); }

  .team-name {
    position: absolute; left: 430px; top: 697px; width: 108px;
    text-align: center; font-size: 15px; line-height: 20px;
    color: var(--burgundy);
  }
</style>
</head>
<body>
<main class="sheet">

  <article class="flyer flyer--left">
    <svg class="flyer__backdrop" viewBox="0 0 571 787" preserveAspectRatio="none" aria-hidden="true">
      <path d="M0 55 C170 10 400 -5 571 5 V215 C430 120 220 105 0 185 Z" fill="var(--gold)"/>
      <path d="M0 100 C200 45 420 45 571 115 V150 C420 85 200 85 0 138 Z" fill="var(--gold-deep)"/>
      <path d="M0 705 C200 690 420 650 571 612 V787 H0 Z" fill="var(--gold)"/>
      <path d="M0 738 C220 722 430 690 571 660 V690 C430 720 220 752 0 765 Z" fill="var(--gold-deep)"/>
    </svg>
    <div class="cheer-squad" role="img" aria-label="Red silhouettes of six jumping cheerleaders with pom-poms"></div>
    <h1 class="headline headline--cheer">CHEER</h1>
    <h1 class="headline headline--championship">CHAMPIONSHIP</h1>
    <svg class="banner" viewBox="0 0 456 100" aria-label="Let's support our cheerleaders!">
      <defs>
        <linearGradient id="ribbonL" x1="0" y1="0" x2="0" y2="1">
          <stop offset="0" stop-color="#e0262c"/><stop offset="1" stop-color="#a5111a"/>
        </linearGradient>
      </defs>
      <path d="M14 40 C150 20 310 22 446 32 L446 90 C310 82 150 84 14 98 Z" fill="var(--shadow-grey)" opacity="0.6"/>
      <path d="M6 30 L34 26 L34 78 L8 84 L18 58 Z" fill="#8c0c12"/>
      <path d="M450 18 L422 16 L422 70 L448 72 L440 46 Z" fill="#8c0c12"/>
      <path d="M24 26 C150 4 300 2 432 12 L432 66 C300 58 150 62 24 84 Z" fill="url(#ribbonL)"/>
      <path id="ribbonLineL" d="M36 70 C150 44 300 38 424 52" fill="none"/>
      <text font-family="Oswald, sans-serif" font-weight="600" font-size="34" fill="var(--white)">
        <textPath href="#ribbonLineL" textLength="384" lengthAdjust="spacingAndGlyphs">LET'S SUPPORT OUR CHEERLEADERS!</textPath>
      </text>
    </svg>
    <p class="event-date event-date__day">SUNDAY</p>
    <p class="event-date event-date__month">OCTOBER 30</p>
    <p class="event-date event-date__year">2011</p>
    <div class="mascot" role="img" aria-label="Team falcon mascot head in burgundy and gold"></div>
    <section class="venue">
      <p class="venue__lead">JOINS US AT</p>
      <p class="venue__line">HARBOR CREST ARENA AT THE PELLHAM COAST COLLEGE</p>
      <p class="venue__line">3870 KESTREL LANE CORAL GABLES, FL 33146</p>
    </section>
    <section class="details details--time">
      <p class="details__label">TIME</p>
      <p>TICKETS ON SALE 8:30AM</p>
      <p>DOORS OPEN 9:00AM</p>
      <p>STARTS 10:00AM</p>
    </section>
    <section class="details details--prices">
      <p class="details__label">PRICES</p>
      <p>ADULTS $10.00</p>
      <p>CHILDREN $5.00</p>
      <p>CASH ONLY</p>
    </section>
    <p class="team-name">TARPON RIDGE FALCONS</p>
  </article>

  <article class="flyer flyer--right">
    <svg class="flyer__backdrop" viewBox="0 0 571 787" preserveAspectRatio="none" aria-hidden="true">
      <path d="M0 55 C170 10 400 -5 571 5 V215 C430 120 220 105 0 185 Z" fill="var(--gold)"/>
      <path d="M0 100 C200 45 420 45 571 115 V150 C420 85 200 85 0 138 Z" fill="var(--gold-deep)"/>
      <path d="M0 705 C200 690 420 650 571 612 V787 H0 Z" fill="var(--gold)"/>
      <path d="M0 738 C220 722 430 690 571 660 V690 C430 720 220 752 0 765 Z" fill="var(--gold-deep)"/>
    </svg>
    <div class="cheer-squad" role="img" aria-label="Red silhouettes of six jumping cheerleaders with pom-poms"></div>
    <h1 class="headline headline--cheer">CHEER</h1>
    <h1 class="headline headline--championship">CHAMPIONSHIP</h1>
    <svg class="banner" viewBox="0 0 456 100" aria-label="Let's support our cheerleaders!">
      <defs>
        <linearGradient id="ribbonR" x1="0" y1="0" x2="0" y2="1">
          <stop offset="0" stop-color="#e0262c"/><stop offset="1" stop-color="#a5111a"/>
        </linearGradient>
      </defs>
      <path d="M14 40 C150 20 310 22 446 32 L446 90 C310 82 150 84 14 98 Z" fill="var(--shadow-grey)" opacity="0.6"/>
      <path d="M6 30 L34 26 L34 78 L8 84 L18 58 Z" fill="#8c0c12"/>
      <path d="M450 18 L422 16 L422 70 L448 72 L440 46 Z" fill="#8c0c12"/>
      <path d="M24 26 C150 4 300 2 432 12 L432 66 C300 58 150 62 24 84 Z" fill="url(#ribbonR)"/>
      <path id="ribbonLineR" d="M36 70 C150 44 300 38 424 52" fill="none"/>
      <text font-family="Oswald, sans-serif" font-weight="600" font-size="34" fill="var(--white)">
        <textPath href="#ribbonLineR" textLength="384" lengthAdjust="spacingAndGlyphs">LET'S SUPPORT OUR CHEERLEADERS!</textPath>
      </text>
    </svg>
    <p class="event-date event-date__day">SUNDAY</p>
    <p class="event-date event-date__month">OCTOBER 30</p>
    <p class="event-date event-date__year">2011</p>
    <div class="mascot" role="img" aria-label="Team falcon mascot head in burgundy and gold"></div>
    <section class="venue">
      <p class="venue__lead">JOINS US AT</p>
      <p class="venue__line">HARBOR CREST ARENA AT THE PELLHAM COAST COLLEGE</p>
      <p class="venue__line">3870 KESTREL LANE CORAL GABLES, FL 33146</p>
    </section>
    <section class="details details--time">
      <p class="details__label">TIME</p>
      <p>TICKETS ON SALE 8:30AM</p>
      <p>DOORS OPEN 9:00AM</p>
      <p>STARTS 10:00AM</p>
    </section>
    <section class="details details--prices">
      <p class="details__label">PRICES</p>
      <p>ADULTS $10.00</p>
      <p>CHILDREN $5.00</p>
      <p>CASH ONLY</p>
    </section>
    <p class="team-name">TARPON RIDGE FALCONS</p>
  </article>

</main>
</body>
</html>
```